Business Stationery Design

I would like to get some stationery designed for my company. The stationery should include a letterhead, envelope, and business card. We are a technology consulting company specializing in Healthcare IT, and Education management systems. The colors of the stationery should match the logo. The logo is uploaded.

Target Market(s)

Hospitals, Clinics. Doctors offices. Private Schools.

Industry/Entity Type

Business

```html
<!DOCTYPE html>
<html lang="en">
<head>
<meta charset="utf-8">
<title>Suncrest Advisory Group – Stationery</title>
<link href="https://fonts.googleapis.com/css2?family=Open+Sans:ital,wght@0,400;0,600;1,400&display=swap" rel="stylesheet">
<style>
  :root {
    --green: #67b81c;
    --green-dark: #58a815;
    --amber: #f2b705;
    --amber-soft: #f7cc45;
    --paper: #ffffff;
    --ink: #3a3a3a;
    --backdrop: #e4e7e6;
  }
  * { box-sizing: border-box; margin: 0; padding: 0; }
  html, body { width: 1200px; height: 900px; overflow: hidden; }
  body {
    background: var(--backdrop);
    font-family: "Open Sans", Arial, sans-serif;
    color: var(--ink);
    position: relative;
  }
  .sheet { position: absolute; background: var(--paper); overflow: hidden; box-shadow: 0 3px 10px rgba(0,0,0,.12); }
  .sheet svg.band { position: absolute; left: 0; bottom: 0; width: 100%; height: 100%; }
  .brand-name { font-weight: 600; color: var(--green); white-space: nowrap; display: flex; align-items: center; gap: 5px; }
  .brand-name .dot { width: 8px; height: 8px; border-radius: 50%; background: var(--amber); flex: none; }
  .brand-name.on-green { color: #fff; }
  .leaf-field { position: absolute; background: var(--amber-soft); border-radius: 6px; }

  /* Letterhead */
  .letterhead { left: 440px; top: 60px; width: 300px; height: 424px; }
  .letterhead .brand-name { position: absolute; top: 30px; left: 0; right: 0; justify-content: center; font-size: 11px; }
  .letterhead .contact { position: absolute; left: 16px; bottom: 10px; font-size: 6.5px; line-height: 1.5; color: #fff; }
  .letterhead .leaf-field { right: 10px; bottom: 6px; width: 70px; height: 30px; }

  /* Folder */
  .folder { left: 790px; top: 60px; width: 300px; height: 424px; background: linear-gradient(160deg, var(--green) 0%, var(--green-dark) 100%); }
  .folder .brand-name { position: absolute; top: 170px; left: 20px; right: 20px; justify-content: center; gap: 10px; }
  .folder .brand-name .dot { width: 16px; height: 16px; }
  .folder .brand-lines { display: flex; flex-direction: column; align-items: flex-end; line-height: 1.1; }
  .folder .brand-main { font-size: 32px; }
  .folder .brand-sub { font-size: 13px; letter-spacing: .5px; }
  .folder .contact { position: absolute; left: 44px; bottom: 48px; font-size: 7.5px; line-height: 1.6; color: #fff; }

  /* Envelope */
  .envelope { left: 440px; top: 560px; width: 460px; height: 230px; }
  .envelope .sender { position: absolute; left: 22px; top: 18px; font-size: 6.5px; line-height: 1.45; }
  .envelope .brand-name { font-size: 9px; margin-bottom: 5px; }
  .envelope .web { color: var(--green); }
  .envelope .leaf-field { left: 8px; top: 130px; width: 80px; height: 40px; }

  /* Business cards */
  .card { width: 220px; height: 126px; }
  .card-front { left: 150px; top: 200px; background: var(--green); }
  .card-front .brand-name { position: absolute; left: 20px; top: 22px; font-size: 11px; }
  .card-front .leaf-field { right: 14px; bottom: 8px; width: 70px; height: 26px; }
  .card-back { left: 150px; top: 360px; }
  .card-back .brand-name { position: absolute; left: 14px; top: 14px; font-size: 8px; }
  .card-back .address { position: absolute; left: 14px; top: 44px; font-size: 5.5px; line-height: 1.45; }
  .card-back .address .web { color: var(--green); }
  .card-back .person { position: absolute; left: 110px; top: 50px; font-size: 5.5px; line-height: 1.45; }
  .card-back .person .name { font-size: 8px; color: var(--green); font-style: italic; }
  .card-back .person .role { font-style: italic; margin-bottom: 6px; }
</style>
</head>
<body>

  <section class="sheet card card-front">
    <svg class="band" viewBox="0 0 220 126" preserveAspectRatio="none" aria-hidden="true">
      <path d="M0,80 Q110,98 220,104 L220,126 L0,126 Z" fill="var(--paper)"/>
      <path d="M0,84 Q110,102 220,108 L220,126 L0,126 Z" fill="var(--amber)"/>
    </svg>
    <div class="brand-name on-green"><span class="dot"></span>Suncrest</div>
    <div class="leaf-field" role="img" aria-label="White leaf pattern"></div>
  </section>

  <section class="sheet card card-back">
    <div class="brand-name"><span class="dot"></span>Suncrest</div>
    <div class="address">
      Street name 1234<br>District area<br>City name 00123<br>
      <span class="web">www.domain.com</span>
    </div>
    <div class="person">
      <div class="name">Mark Ellison</div>
      <div class="role">General Manager</div>
      Phone: +00 (1) 234 56 78<br>
      Mobile: +00 (1) 234 56 78<br>
      Email: name@domain.com
    </div>
  </section>

  <section class="sheet letterhead">
    <div class="brand-name"><span class="dot"></span>Suncrest Advisory Group</div>
    <svg class="band" viewBox="0 0 300 424" preserveAspectRatio="none" aria-hidden="true">
      <path d="M0,352 Q150,372 300,398 L300,424 L0,424 Z" fill="var(--green)"/>
      <path d="M0,360 Q150,381 300,406 L300,424 L0,424 Z" fill="var(--amber)"/>
    </svg>
    <div class="contact">
      Street name 1234 &nbsp;|&nbsp; District area &nbsp;|&nbsp; City name 00123<br>
      Phone: +00 (1) 234 56 78 &nbsp;|&nbsp; www.domainname.com
    </div>
    <div class="leaf-field" role="img" aria-label="White leaf pattern"></div>
  </section>

  <section class="sheet folder">
    <div class="brand-name on-green">
      <span class="dot"></span>
      <span class="brand-lines">
        <span class="brand-main">Suncrest</span>
        <span class="brand-sub">Advisory Group</span>
      </span>
    </div>
    <div class="contact">
      Street name 1234 &nbsp;|&nbsp; District area &nbsp;|&nbsp; City name 00123<br>
      Phone: +00 (1) 234 56 78 &nbsp;|&nbsp; www.domainname.com
    </div>
  </section>

  <section class="sheet envelope">
    <div class="sender">
      <div class="brand-name"><span class="dot"></span>Suncrest</div>
      Street name 1234<br>District area<br>City name 00123<br>
      <span class="web">www.domain.com</span>
    </div>
    <svg class="band" viewBox="0 0 460 230" preserveAspectRatio="none" aria-hidden="true">
      <path d="M0,118 C160,150 340,190 460,230 L0,230 Z" fill="var(--green)"/>
      <path d="M0,126 C150,160 320,196 440,230 L0,230 Z" fill="var(--amber)"/>
      <path d="M0,178 C120,200 220,216 300,230 L0,230 Z" fill="var(--paper)"/>
    </svg>
    <div class="leaf-field" role="img" aria-label="White leaf pattern"></div>
  </section>

</body>
</html>
```